Financial Planning Business needs a business card design

We need a business card design that is for a new financial planning business based in Australia. We provide financial planning advice such as retirement planning, wealth creation, asset protection.

Attached is the logo design. On the front side of the business card needs to incorporate the following:
- adviser name
- adviser title (ie Managing Director)
- address
- phone number
- email
- website address

Ideally it should also have the business name and logo

On the back of the card I would like this to be black in colour with the business name and logo

I have been advised the font is "Cinzel" (regular and bold)

Industry/Entity Type

Financial

Requirements
Must have
• Logo and business name

Format to have as follows:
Ben xxxxxxxx
Managing Director / Senior Financial Adviser
address
phone email
website

```html
<!DOCTYPE html>
<html lang="en">
<head>
<meta charset="utf-8">
<title>Meridian Wealth Planning – Business Card</title>
<link href="https://fonts.googleapis.com/css2?family=Cinzel:wght@400;700&family=Cabin:wght@400&display=swap" rel="stylesheet">
<style>
  :root {
    --stage: #e8e6e3;
    --card-front: #ffffff;
    --card-back: #000000;
    --brand-blue: #0a99cf;
    --ink: #2b2b2b;
    --ink-soft: #555555;
    --rule: #a9a9a9;
    --mark-grey: #9a9a9a;
    --back-text: #ffffff;
  }
  * { box-sizing: border-box; margin: 0; padding: 0; }
  html, body {
    width: 1200px; height: 1155px; overflow: hidden;
    background: var(--stage);
  }
  .canvas { position: relative; width: 1200px; height: 1155px; }

  .card { position: absolute; width: 912px; height: 522px; }
  .card--front {
    left: 236px; top: 34px;
    background: var(--card-front);
    border: 1px solid #8a8a8a;
  }
  .card--back {
    left: 38px; top: 601px;
    background: var(--card-back);
  }

  /* Brand block on the front */
  .brand {
    position: absolute; left: 30px; top: 226px;
    display: flex; align-items: center; gap: 18px;
  }
  .brand__square {
    width: 96px; height: 96px; background: var(--mark-grey);
  }
  .brand__name {
    font-family: "Cinzel", serif; font-weight: 400;
    color: var(--brand-blue); line-height: 1;
  }
  .brand__name-main { display: block; font-size: 62px; letter-spacing: 1px; }
  .brand__name-sub { display: block; font-size: 27px; margin-top: 6px; letter-spacing: 0.5px; }

  .divider {
    position: absolute; left: 492px; top: 96px;
    width: 2px; height: 325px; background: var(--rule);
  }

  .contact { position: absolute; left: 518px; top: 96px; }
  .contact__name {
    font-family: "Cinzel", serif; font-weight: 400;
    font-size: 33px; color: var(--brand-blue); line-height: 1.2;
  }
  .contact__title {
    font-family: "Cinzel", serif; font-weight: 400;
    font-size: 27px; color: var(--ink-soft); line-height: 1.2; margin-top: 2px;
  }
  .contact__list { list-style: none; margin-top: 18px; }
  .contact__item {
    display: flex; align-items: center; gap: 8px;
    font-family: "Cabin", sans-serif; font-size: 22px; color: var(--ink);
    height: 35.5px;
  }
  .contact__icon { width: 20px; height: 20px; flex: none; }
  .contact__address {
    font-family: "Cabin", sans-serif; font-size: 20.5px; color: var(--ink);
    line-height: 32px; margin-top: 12px; font-style: normal;
  }

  /* Back */
  .back-brand {
    position: absolute; left: 0; right: 0; top: 170px;
    text-align: center;
    font-family: "Cinzel", serif; font-weight: 400;
    color: var(--mark-grey); line-height: 1;
  }
  .back-brand__main { display: block; font-size: 86px; letter-spacing: 2px; }
  .back-brand__sub { display: block; font-size: 38px; margin-top: 14px; letter-spacing: 1px; }
  .back-web {
    position: absolute; left: 0; right: 0; top: 448px;
    text-align: center;
    font-family: "Cabin", sans-serif; font-size: 29px;
    letter-spacing: 3px; color: var(--back-text);
  }
</style>
</head>
<body>
<main class="canvas">

  <section class="card card--front" aria-label="Card front">
    <div class="brand">
      <div class="brand__square"></div>
      <p class="brand__name">
        <span class="brand__name-main">Meridian</span>
        <span class="brand__name-sub">Wealth Planning</span>
      </p>
    </div>

    <div class="divider"></div>

    <div class="contact">
      <h1 class="contact__name">Your Name</h1>
      <p class="contact__title">Title</p>
      <ul class="contact__list">
        <li class="contact__item">
          <svg class="contact__icon" viewBox="0 0 20 20" aria-hidden="true">
            <circle cx="10" cy="10" r="8.5" fill="none" stroke="var(--brand-blue)" stroke-width="2"/>
            <path d="M7 5.5l2 2-1 1.5c.6 1.4 1.6 2.4 3 3l1.5-1 2 2-1.3 1.5C9.5 14 6 10.5 5.5 6.8z" fill="var(--brand-blue)"/>
          </svg>
          012-345-6789
        </li>
        <li class="contact__item">
          <svg class="contact__icon" viewBox="0 0 20 20" aria-hidden="true">
            <rect x="5" y="3" width="10" height="7" rx="1" fill="var(--brand-blue)"/>
            <path d="M1 11a3 3 0 0 1 3-3h12a3 3 0 0 1 3 3v6H1z" fill="var(--brand-blue)"/>
          </svg>
          012-345-6789
        </li>
        <li class="contact__item">
          <svg class="contact__icon" viewBox="0 0 20 20" aria-hidden="true">
            <rect x="2" y="4" width="16" height="12" rx="1" fill="var(--brand-blue)"/>
            <path d="M4 7l6 4 6-4" fill="none" stroke="#fff" stroke-width="1.6"/>
          </svg>
          info@meridianwealthplanning.com
        </li>
        <li class="contact__item">
          <svg class="contact__icon" viewBox="0 0 20 20" aria-hidden="true">
            <circle cx="10" cy="10" r="8.5" fill="var(--brand-blue)"/>
            <path d="M2 10h16M10 2c-3 3-3 13 0 16M10 2c3 3 3 13 0 16M4 6h12M4 14h12" fill="none" stroke="#fff" stroke-width="1"/>
          </svg>
          www.meridianwealthplanning.com
        </li>
      </ul>
      <address class="contact__address">
        Sreet Name, City Name<br>
        Zip Code-00000
      </address>
    </div>
  </section>

  <section class="card card--back" aria-label="Card back">
    <p class="back-brand">
      <span class="back-brand__main">Meridian</span>
      <span class="back-brand__sub">Wealth Planning</span>
    </p>
    <p class="back-web">www.meridianwealthplanning.com</p>
  </section>

</main>
</body>
</html>
```